Vardel Mechanical Services Cultural Norms

Tale the uploaded list of cultural norms and develop a design that showcases how these 8 items encompass everything about our companies culture.

```html
<!DOCTYPE html>
<html lang="en">
<head>
<meta charset="utf-8">
<title>Vardel Mechanical Services – Cultural Norms</title>
<link rel="stylesheet" href="https://fonts.googleapis.com/css2?family=Oswald:wght@500;600;700&family=Arimo:wght@400;700&display=swap">
<style>
  :root {
    --backdrop: #3b2f1f;
    --paper: #f4f2ee;
    --ink: #111111;
    --gold: #8b7348;
    --white: #ffffff;
  }
  * { box-sizing: border-box; margin: 0; padding: 0; }
  html, body { width: 1200px; height: 1200px; overflow: hidden; }
  body { background: var(--backdrop); position: relative; font-family: "Arimo", Arial, sans-serif; color: var(--ink); }

  .poster {
    position: absolute; left: 218px; top: 64px; width: 764px; height: 1071px;
    background: var(--paper); overflow: hidden;
    box-shadow: 0 4px 18px rgba(0,0,0,0.35);
  }

  .hero {
    position: absolute; left: 0; top: 0; width: 764px; height: 202px;
    background:
      linear-gradient(90deg, rgba(245,245,247,0.95) 0%, rgba(235,235,238,0.75) 30%, rgba(200,198,200,0.25) 55%, rgba(0,0,0,0) 70%),
      linear-gradient(90deg, #dcdcdf 0%, #c8c5c2 45%, #9f948a 65%, #7a6a5a 85%, #6b5c4d 100%);
  }
  .hero-band { position: absolute; left: 0; top: 202px; width: 764px; height: 8px; background: var(--gold); }

  .brand {
    position: absolute; left: 24px; top: 52px; display: flex; align-items: center; gap: 12px;
  }
  .brand-dot { width: 34px; height: 34px; border-radius: 50%; background: var(--ink); flex: none; }
  .brand-name {
    font-family: "Oswald", "Arial Narrow", sans-serif; font-weight: 600; font-size: 26px;
    line-height: 1.05; text-transform: uppercase; color: var(--ink); width: 240px; letter-spacing: 0.5px;
  }

  .page-title {
    position: absolute; right: 25px; top: 22px; text-align: right;
    font-family: "Oswald", "Arial Narrow", sans-serif; font-weight: 700; font-size: 48px;
    line-height: 46px; color: var(--white); text-transform: uppercase; letter-spacing: 0.5px;
  }
  .page-title-rule { position: absolute; left: 568px; top: 117px; width: 171px; height: 2px; background: var(--white); }

  .flow { position: absolute; left: 0; top: 0; width: 764px; height: 1071px; }

  .norm-number {
    position: absolute; width: 60px; text-align: center;
    font-family: "Arimo", Arial, sans-serif; font-weight: 700; font-size: 65px; line-height: 1;
    color: var(--gold);
  }
  .norm {
    position: absolute; width: 304px;
  }
  .norm--right { left: 342px; text-align: justify; }
  .norm--left { left: 118px; width: 307px; text-align: justify; text-align-last: right; }
  .norm--left .norm-title { text-align: right; }
  .norm-title {
    font-family: "Oswald", "Arial Narrow", sans-serif; font-weight: 600; font-size: 18.5px;
    line-height: 24px; color: var(--ink);
  }
  .norm-title .accent { color: var(--gold); }
  .norm-text { font-size: 13.2px; line-height: 17.4px; margin-top: 2px; }

  .footer-bar { position: absolute; left: 0; top: 1048px; width: 764px; height: 23px; background: var(--ink); }
</style>
</head>
<body>
  <main class="poster">
    <div class="hero" role="img" aria-label="Photo of a technician in a white shirt and black glove turning a large belt pulley on machinery"></div>
    <div class="hero-band"></div>

    <div class="brand">
      <span class="brand-dot"></span>
      <span class="brand-name">Vardel Mechanical Services</span>
    </div>

    <h1 class="page-title">Cultural<br>Norms</h1>
    <div class="page-title-rule"></div>

    <svg class="flow" viewBox="0 0 764 1071" aria-hidden="true">
      <g fill="none" stroke="#111" stroke-width="1.6">
        <!-- odd boxes (right) -->
        <path d="M300,228.5 H627 A30,30 0 0 1 657,258.5 V298.1 A30,30 0 0 1 627,328.1 H300 Z"/>
        <path d="M300,427.7 H627 A30,30 0 0 1 657,457.7 V497.3 A30,30 0 0 1 627,527.3 H300 Z"/>
        <path d="M300,626.9 H627 A30,30 0 0 1 657,656.9 V696.5 A30,30 0 0 1 627,726.5 H300 Z"/>
        <path d="M300,826.1 H627 A30,30 0 0 1 657,856.1 V895.7 A30,30 0 0 1 627,925.7 H300 Z"/>
        <!-- even boxes (left) -->
        <path d="M464,328.1 H140 A30,30 0 0 0 110,358.1 V397.7 A30,30 0 0 0 140,427.7 H464 V393.9 L444,377.9 L464,361.9 Z"/>
        <path d="M464,527.3 H140 A30,30 0 0 0 110,557.3 V596.9 A30,30 0 0 0 140,626.9 H464 V593.1 L444,577.1 L464,561.1 Z"/>
        <path d="M464,726.5 H140 A30,30 0 0 0 110,756.5 V796.1 A30,30 0 0 0 140,826.1 H464 V792.3 L444,776.3 L464,760.3 Z"/>
        <path d="M464,925.7 H140 A30,30 0 0 0 110,955.7 V995.3 A30,30 0 0 0 140,1025.3 H464 V991.5 L444,975.5 L464,959.5 Z"/>
        <!-- start and end leads -->
        <path d="M300,228.5 H140 A30,30 0 0 0 110,258.5 V312"/>
        <path d="M464,1025.3 H623 A30,30 0 0 0 653,995.3 V942"/>
      </g>
      <circle cx="110" cy="312" r="4" fill="#111"/>
      <circle cx="653" cy="942" r="4" fill="#111"/>

      <!-- black notches under left boxes -->
      <g>
        <polygon points="228,427.7 241.6,444 255,427.7" fill="#f4f2ee"/>
        <polyline points="228,427.7 241.6,444 255,427.7" fill="none" stroke="#111" stroke-width="1.6"/>
        <polygon points="228,626.9 241.6,643 255,626.9" fill="#f4f2ee"/>
        <polyline points="228,626.9 241.6,643 255,626.9" fill="none" stroke="#111" stroke-width="1.6"/>
        <polygon points="228,826.1 241.6,842 255,826.1" fill="#f4f2ee"/>
        <polyline points="228,826.1 241.6,842 255,826.1" fill="none" stroke="#111" stroke-width="1.6"/>
      </g>

      <!-- gold chevrons and notches -->
      <g fill="none" stroke="#8b7348" stroke-width="5" stroke-linejoin="miter">
        <polyline points="299,260 321,278.3 299,296.6"/>
        <polyline points="299,459.2 321,477.5 299,495.8"/>
        <polyline points="299,658.4 321,676.7 299,695"/>
        <polyline points="299,857.6 321,875.9 299,894.2"/>
        <polyline points="499,328.1 515,350 531,328.1"/>
        <polyline points="499,527.3 515,549 531,527.3"/>
        <polyline points="499,726.5 515,748 531,726.5"/>
        <polyline points="499,925.7 515,947 531,925.7"/>
      </g>

      <!-- icon pills -->
      <g fill="#111">
        <path d="M220.6,251.3 H183 A27,27 0 0 0 183,305.3 H220.6 Z"/>
        <path d="M541.8,350.9 H580 A27,27 0 0 1 580,404.9 H541.8 Z"/>
        <path d="M220.6,450.5 H183 A27,27 0 0 0 183,504.5 H220.6 Z"/>
        <path d="M541.8,550.1 H580 A27,27 0 0 1 580,604.1 H541.8 Z"/>
        <path d="M220.6,649.7 H183 A27,27 0 0 0 183,703.7 H220.6 Z"/>
        <path d="M541.8,749.3 H580 A27,27 0 0 1 580,803.3 H541.8 Z"/>
        <path d="M220.6,848.9 H183 A27,27 0 0 0 183,902.9 H220.6 Z"/>
        <path d="M541.8,948.5 H580 A27,27 0 0 1 580,1002.5 H541.8 Z"/>
      </g>

      <!-- icons -->
      <g stroke="#fff" fill="none" stroke-width="1.8" stroke-linecap="round" stroke-linejoin="round">
        <!-- 1 improvement -->
        <g transform="translate(190,278.3)">
          <path d="M-14,-8 A16,16 0 0 1 10,-13"/><path d="M14,8 A16,16 0 0 1 -10,13"/>
          <polyline points="6,-15 10,-13 8,-9"/><polyline points="-6,15 -10,13 -8,9"/>
          <path d="M-7,7 V-2 M-10,1 L-7,-3 L-4,1 M0,7 V-6 M-3,-3 L0,-7 L3,-3 M7,7 V-2 M4,1 L7,-3 L10,1"/>
          <path d="M-10,9 H10"/>
        </g>
        <!-- 2 people with stars -->
        <g transform="translate(573,377.9)" fill="#fff" stroke="none">
          <polygon points="-12,-16 -10.5,-12.5 -7,-12.5 -9.8,-10.3 -8.8,-7 -12,-9 -15.2,-7 -14.2,-10.3 -17,-12.5 -13.5,-12.5"/>
          <polygon points="0,-18 1.5,-14.5 5,-14.5 2.2,-12.3 3.2,-9 0,-11 -3.2,-9 -2.2,-12.3 -5,-14.5 -1.5,-14.5"/>
          <polygon points="12,-16 13.5,-12.5 17,-12.5 14.2,-10.3 15.2,-7 12,-9 8.8,-7 9.8,-10.3 7,-12.5 10.5,-12.5"/>
          <circle cx="-10" cy="0" r="3.2"/><circle cx="10" cy="0" r="3.2"/><circle cx="0" cy="1" r="4"/>
          <path d="M-16,12 A6,6 0 0 1 -4,12 Z"/><path d="M4,12 A6,6 0 0 1 16,12 Z"/>
          <path d="M-8,16 A8,8 0 0 1 8,16 Z"/>
        </g>
        <!-- 3 encouragement -->
        <g transform="translate(190,477.5)" fill="#fff" stroke="none">
          <circle cx="0" cy="-14" r="4"/>
          <path d="M-12,-18 L-3,-8 H3 L12,-18 L14,-16 L5,-5 V0 H-5 V-5 L-14,-16 Z"/>
          <circle cx="0" cy="4" r="3.5"/>
          <path d="M-9,18 V11 A4,4 0 0 1 -5,8 H5 A4,4 0 0 1 9,11 V18 Z"/>
        </g>
        <!-- 4 communication -->
        <g transform="translate(573,577.1)">
          <path d="M-11,-18 H5 A3,3 0 0 1 8,-15 V-5 A3,3 0 0 1 5,-2 H-3 L-7,2 V-2 H-11 A3,3 0 0 1 -14,-5 V-15 A3,3 0 0 1 -11,-18 Z" fill="#fff" stroke="none"/>
          <polyline points="-8,-10 -4,-6 3,-13" stroke="#111" stroke-width="2"/>
          <path d="M11,-14 A5,5 0 0 1 14,-6 L11,-3" />
          <g fill="#fff" stroke="none">
            <circle cx="-10" cy="6" r="3.5"/><path d="M-16,18 A6,6 0 0 1 -4,18 Z"/>
            <circle cx="10" cy="6" r="3.5"/><path d="M4,18 A6,6 0 0 1 16,18 Z"/>
          </g>
        </g>
        <!-- 5 ownership: hand with gear -->
        <g transform="translate(190,676.7)">
          <circle cx="8" cy="-10" r="5"/>
          <path d="M8,-18 V-15 M8,-5 V-2 M0,-10 H3 M13,-10 H16 M2.5,-15.5 L4.5,-13.5 M11.5,-6.5 L13.5,-4.5 M13.5,-15.5 L11.5,-13.5 M4.5,-6.5 L2.5,-4.5"/>
          <rect x="-17" y="2" width="7" height="14" rx="1" fill="#fff" transform="rotate(-15 -13 9)"/>
          <path d="M-9,4 Q-3,0 3,3 L8,4 M-8,13 H4 L16,3 Q14,0 11,2 L5,6"/>
        </g>
        <!-- 6 stairs -->
        <g transform="translate(573,776.3)">
          <polyline points="-10,18 -4,18 -4,12 2,12 2,6 8,6 8,0 14,0"/>
          <circle cx="-8" cy="-16" r="3" fill="#fff" stroke="none"/>
          <path d="M-8,-11 V0 M-8,-9 L-3,-4 M-8,-9 L-13,-3 M-8,0 L-4,8 M-8,0 L-12,9" stroke-width="2.4"/>
        </g>
        <!-- 7 handshake -->
        <g transform="translate(190,875.9)">
          <path d="M-18,-8 L-12,-12 L-4,2 L-10,6 Z" fill="#fff" stroke="none"/>
          <path d="M18,-8 L12,-12 L4,2 L10,6 Z" fill="#fff" stroke="none"/>
          <path d="M-9,-7 L-2,-9 L6,-3 L1,0 M-4,3 L2,9 M-1,0 L5,6 M2,-3 L8,3 M8,-6 L2,-9"/>
        </g>
        <!-- 8 badge -->
        <g transform="translate(573,975.5)">
          <circle cx="0" cy="-4" r="11"/>
          <circle cx="0" cy="-4" r="6.5"/>
          <polygon points="0,-8 1.2,-5.5 4,-5.5 1.8,-3.8 2.6,-1 0,-2.6 -2.6,-1 -1.8,-3.8 -4,-5.5 -1.2,-5.5" fill="#fff" stroke="none"/>
          <path d="M-6,6 L-10,17 L-6,15 L-4,18 L-1,8 M6,6 L10,17 L6,15 L4,18 L1,8"/>
        </g>
      </g>
    </svg>

    <span class="norm-number" style="left:235px;top:247px;">1</span>
    <span class="norm-number" style="left:466px;top:347px;">2</span>
    <span class="norm-number" style="left:235px;top:446px;">3</span>
    <span class="norm-number" style="left:466px;top:546px;">4</span>
    <span class="norm-number" style="left:235px;top:645px;">5</span>
    <span class="norm-number" style="left:466px;top:745px;">6</span>
    <span class="norm-number" style="left:235px;top:844px;">7</span>
    <span class="norm-number" style="left:466px;top:944px;">8</span>

    <section class="norm norm--right" style="top:243px;">
      <h2 class="norm-title">Continuous <span class="accent">Improvement:</span></h2>
      <p class="norm-text">We believe that there is always room for improvement in everything we do.</p>
    </section>
    <section class="norm norm--left" style="top:343px;">
      <h2 class="norm-title">Enhancing <span class="accent">Lives:</span></h2>
      <p class="norm-text">Our aim is to positively impact the lives of others through our actions and services.</p>
    </section>
    <section class="norm norm--right" style="top:435px;">
      <h2 class="norm-title">Cultivating <span class="accent">Encouragement:</span></h2>
      <p class="norm-text">We believe that fostering encouragement among our team members leads to personal fulfillment and opportunity.</p>
    </section>
    <section class="norm norm--left" style="top:535px;">
      <h2 class="norm-title">Effective <span class="accent">Communication:</span></h2>
      <p class="norm-text">We embrace the challenge of effective communication, recognizing its importance in our success.</p>
    </section>
    <section class="norm norm--right" style="top:643px;">
      <h2 class="norm-title">Think. Act. <span class="accent">Take Ownership:</span></h2>
      <p class="norm-text">We operate by the mantra of thinking critically, executing, and taking ownership of our decisions.</p>
    </section>
    <section class="norm norm--left" style="top:743px;">
      <h2 class="norm-title">Stay 1 Step <span class="accent">Ahead:</span></h2>
      <p class="norm-text">We strive to stay one step ahead, anticipating needs and proactively addressing challenges.</p>
    </section>
    <section class="norm norm--right" style="top:834px;">
      <h2 class="norm-title">Creating <span class="accent">Healthy Environments:</span></h2>
      <p class="norm-text">We are committed to establishing comfortable environments where our clients can thrive and be productive.</p>
    </section>
    <section class="norm norm--left" style="top:934px;">
      <h2 class="norm-title">Setting <span class="accent">Higher Standards:</span></h2>
      <p class="norm-text">We aim to elevate the standards of the mechanical industry by educating both our customers and ourselves, constantly raising the bar.</p>
    </section>

    <div class="footer-bar"></div>
    <svg style="position:absolute;left:0;top:1030px;" width="764" height="41" viewBox="0 0 764 41" aria-hidden="true">
      <path d="M521,41 L535,16 Q540,9 548,9 H764 V41 Z" fill="#8b7348"/>
      <path d="M515,41 L532,18" stroke="#f4f2ee" stroke-width="4"/>
    </svg>
  </main>
</body>
</html>
```